New Coffee Packaging

Update/refresh/modernize range of 1 kg Coffee packaging

Industry/Entity Type

Hospitalty

Requirements
Must have
• Clean. crisp, eye catching
Nice to have
• Verdano means 'Height' specialty coffee is grown at high altitudes, peaks. mountains

```html
<!DOCTYPE html>
<html lang="en">
<head>
<meta charset="utf-8">
<title>Verdano Coffee Co. – 1kg Range</title>
<link rel="stylesheet" href="https://fonts.googleapis.com/css2?family=Cabin:wght@400;600;700&family=Montserrat:wght@600&display=swap">
<style>
  :root{
    --stage:#ecebe6;
    --bag-fold:#161616;
    --bag-body:#232323;
    --panel:#231f20;
    --ink-light:#e9e9ea;
    --ink-soft:#cfcfcf;
    --rule:#5a5a5a;
    --gold:#c98a1b;
    --gold-deep:#6e4c12;
    --green:#6aac3a;
    --green-deep:#2f5a1c;
    --blue:#2d3f9a;
    --blue-deep:#161e4c;
    --red:#d3263a;
    --red-deep:#6c1420;
  }
  *{margin:0;padding:0;box-sizing:border-box}
  html,body{width:1200px;height:3000px;overflow:hidden}
  body{position:relative;background:var(--stage);font-family:"Cabin",sans-serif;color:var(--ink-light)}

  .range-row{position:absolute;left:0;width:1200px;height:1200px;background:var(--stage)}
  .range-row--top{top:0}
  .range-row--bottom{top:1200px}

  .bag{position:absolute;top:120px;width:360px;height:960px;box-shadow:0 18px 40px rgba(0,0,0,.25);border-radius:6px 6px 2px 2px}
  .bag--left{left:170px}
  .bag--right{left:670px}
  .bag--gold{--accent:var(--gold);--accent-deep:var(--gold-deep);--label-bg:var(--gold);--label-text:#2a2a2a}
  .bag--green{--accent:var(--green);--accent-deep:var(--green-deep);--label-bg:var(--green);--label-text:#fff}
  .bag--blue{--accent:var(--blue);--accent-deep:var(--blue-deep);--label-bg:var(--blue);--label-text:#9aa6e0}
  .bag--red{--accent:var(--red);--accent-deep:var(--red-deep);--label-bg:var(--red);--label-text:#fff}

  .bag__fold{position:absolute;top:0;left:0;width:100%;height:70px;background:linear-gradient(180deg,#222 0%,var(--bag-fold) 100%);border-radius:6px 6px 0 0}
  .bag__body{position:absolute;top:70px;left:0;width:100%;height:890px;background:var(--bag-body);overflow:hidden}
  .bag__pattern{position:absolute;top:30px;bottom:0;width:62px;
    background:linear-gradient(180deg,var(--accent) 0%,var(--accent-deep) 55%,var(--accent) 100%)}
  .bag__pattern--left{left:0}
  .bag__pattern--right{right:0}

  .bag__content{position:absolute;left:62px;right:62px;top:0;height:100%;text-align:center}
  .bag__kiwi{position:absolute;left:50%;top:78px;width:76px;height:48px;margin-left:-38px;background:var(--accent);border-radius:50% 50% 40% 40%}
  .bag__brand{position:absolute;top:160px;left:0;right:0;font-weight:700;font-size:58px;line-height:1;color:var(--ink-light)}
  .bag__sub{position:absolute;top:240px;left:0;right:0;font-size:22px;letter-spacing:4px;color:var(--ink-soft)}
  .bag__label{position:absolute;top:300px;left:18px;right:18px;height:44px;background:var(--label-bg);
    font-family:"Montserrat",sans-serif;font-weight:600;font-size:20px;letter-spacing:6px;line-height:44px;color:var(--label-text)}
  .bag__profile{position:absolute;top:385px;left:20px;right:20px}
  .bag__profile-title{font-weight:600;font-size:14px;padding-bottom:10px;border-bottom:1px solid var(--rule)}
  .bag__notes{list-style:none;padding:12px 0;font-size:15px;line-height:22px;border-bottom:1px solid var(--rule)}
  .bag__methods{position:absolute;top:590px;left:6px;right:6px;display:flex;justify-content:space-between}
  .method{width:52px;font-size:11px;color:var(--ink-soft)}
  .method svg{display:block;margin:0 auto 4px;width:30px;height:30px}
  .bag__url{position:absolute;top:680px;left:0;right:0;font-weight:700;font-size:15px;letter-spacing:.5px;color:var(--accent)}
  .bag__weight{position:absolute;top:712px;left:0;right:0;font-weight:700;font-size:30px;color:var(--accent)}

  .bag--blue .bag__brand,.bag--blue .bag__sub,.bag--blue .bag__notes,.bag--blue .bag__profile-title,.bag--blue .method{opacity:.85}

  .brand-panel{position:absolute;top:2400px;left:0;width:1200px;height:600px;background:var(--panel)}
  .brand-panel__totem{position:absolute;top:45px;width:124px;height:555px;
    background:linear-gradient(180deg,var(--gold) 0%,#a8721a 50%,var(--gold) 100%)}
  .brand-panel__totem--left{left:254px}
  .brand-panel__totem--right{left:842px}
  .brand-panel__kiwi{position:absolute;top:150px;left:545px;width:150px;height:105px;background:var(--gold);border-radius:50% 50% 40% 40%}
  .brand-panel__name{position:absolute;top:320px;left:0;width:1200px;text-align:center;font-weight:700;font-size:120px;line-height:1;color:#fff}
  .brand-panel__sub{position:absolute;top:505px;left:0;width:1200px;text-align:center;font-weight:400;font-size:44px;letter-spacing:8px;color:#fff}
</style>
</head>
<body>

<section class="range-row range-row--top">
  <article class="bag bag--left bag--gold">
    <div class="bag__fold"></div>
    <div class="bag__body">
      <div class="bag__pattern bag__pattern--left" role="img" aria-label="Carved totem head above a vertical koru pattern in gold"></div>
      <div class="bag__pattern bag__pattern--right" role="img" aria-label="Carved totem head above a vertical koru pattern in gold"></div>
      <div class="bag__content">
        <div class="bag__kiwi" role="img" aria-label="Kiwi bird illustration in gold"></div>
        <div class="bag__brand">Verdano</div>
        <div class="bag__sub">coffee co.</div>
        <div class="bag__label">SUPREME</div>
        <div class="bag__profile">
          <div class="bag__profile-title">CUP PROFILE:</div>
          <ul class="bag__notes"><li>Honey</li><li>Stonefruit</li><li>Toffee</li><li>Medium/high sweetness</li></ul>
        </div>
        <div class="bag__methods">
          <div class="method"><svg viewBox="0 0 30 30" fill="none" stroke="#ccc" stroke-width="2"><path d="M4 6h22L17 20h-4z"/><path d="M11 25h8"/></svg>Filter</div>
          <div class="method"><svg viewBox="0 0 30 30" fill="none" stroke="#ccc" stroke-width="2"><circle cx="9" cy="9" r="6"/><path d="M13 13l13 13"/></svg>Espresso</div>
          <div class="method"><svg viewBox="0 0 30 30" fill="none" stroke="#ccc" stroke-width="2"><rect x="8" y="8" width="14" height="19"/><path d="M15 2v12M10 3h10"/></svg>Plunger</div>
          <div class="method"><svg viewBox="0 0 30 30" fill="#ccc"><ellipse cx="11" cy="9" rx="5" ry="7"/><ellipse cx="20" cy="21" rx="5" ry="7"/></svg>Beans</div>
        </div>
        <div class="bag__url">www.verdanocoffee.co.nz</div>
        <div class="bag__weight">1Kg</div>
      </div>
    </div>
  </article>

  <article class="bag bag--right bag--green">
    <div class="bag__fold"></div>
    <div class="bag__body">
      <div class="bag__pattern bag__pattern--left" role="img" aria-label="Carved totem head above a vertical koru pattern in green"></div>
      <div class="bag__pattern bag__pattern--right" role="img" aria-label="Carved totem head above a vertical koru pattern in green"></div>
      <div class="bag__content">
        <div class="bag__kiwi" role="img" aria-label="Kiwi bird illustration in green"></div>
        <div class="bag__brand">Verdano</div>
        <div class="bag__sub">coffee co.</div>
        <div class="bag__label">ORGANIC</div>
        <div class="bag__profile">
          <div class="bag__profile-title">CUP PROFILE:</div>
          <ul class="bag__notes"><li>Honey</li><li>Stonefruit</li><li>Toffee</li><li>Medium/high sweetness</li></ul>
        </div>
        <div class="bag__methods">
          <div class="method"><svg viewBox="0 0 30 30" fill="none" stroke="#ccc" stroke-width="2"><path d="M4 6h22L17 20h-4z"/><path d="M11 25h8"/></svg>Filter</div>
          <div class="method"><svg viewBox="0 0 30 30" fill="none" stroke="#ccc" stroke-width="2"><circle cx="9" cy="9" r="6"/><path d="M13 13l13 13"/></svg>Espresso</div>
          <div class="method"><svg viewBox="0 0 30 30" fill="none" stroke="#ccc" stroke-width="2"><rect x="8" y="8" width="14" height="19"/><path d="M15 2v12M10 3h10"/></svg>Plunger</div>
          <div class="method"><svg viewBox="0 0 30 30" fill="#ccc"><ellipse cx="11" cy="9" rx="5" ry="7"/><ellipse cx="20" cy="21" rx="5" ry="7"/></svg>Beans</div>
        </div>
        <div class="bag__url">www.verdanocoffee.co.nz</div>
        <div class="bag__weight">1Kg</div>
      </div>
    </div>
  </article>
</section>

<section class="range-row range-row--bottom">
  <article class="bag bag--left bag--blue">
    <div class="bag__fold"></div>
    <div class="bag__body">
      <div class="bag__pattern bag__pattern--left" role="img" aria-label="Carved totem head above a vertical fern pattern in deep blue"></div>
      <div class="bag__pattern bag__pattern--right" role="img" aria-label="Carved totem head above a vertical fern pattern in deep blue"></div>
      <div class="bag__content">
        <div class="bag__kiwi" role="img" aria-label="Kiwi bird illustration in deep blue"></div>
        <div class="bag__brand">Verdano</div>
        <div class="bag__sub">coffee co.</div>
        <div class="bag__label">ECLIPSE</div>
        <div class="bag__profile">
          <div class="bag__profile-title">CUP PROFILE:</div>
          <ul class="bag__notes"><li>Honey</li><li>Stonefruit</li><li>Toffee</li><li>Medium/high sweetness</li></ul>
        </div>
        <div class="bag__methods">
          <div class="method"><svg viewBox="0 0 30 30" fill="none" stroke="#ccc" stroke-width="2"><path d="M4 6h22L17 20h-4z"/><path d="M11 25h8"/></svg>Filter</div>
          <div class="method"><svg viewBox="0 0 30 30" fill="none" stroke="#ccc" stroke-width="2"><circle cx="9" cy="9" r="6"/><path d="M13 13l13 13"/></svg>Espresso</div>
          <div class="method"><svg viewBox="0 0 30 30" fill="none" stroke="#ccc" stroke-width="2"><rect x="8" y="8" width="14" height="19"/><path d="M15 2v12M10 3h10"/></svg>Plunger</div>
          <div class="method"><svg viewBox="0 0 30 30" fill="#ccc"><ellipse cx="11" cy="9" rx="5" ry="7"/><ellipse cx="20" cy="21" rx="5" ry="7"/></svg>Beans</div>
        </div>
        <div class="bag__url">www.verdanocoffee.co.nz</div>
        <div class="bag__weight">1Kg</div>
      </div>
    </div>
  </article>

  <article class="bag bag--right bag--red">
    <div class="bag__fold"></div>
    <div class="bag__body">
      <div class="bag__pattern bag__pattern--left" role="img" aria-label="Carved totem head above a vertical spiral pattern in red"></div>
      <div class="bag__pattern bag__pattern--right" role="img" aria-label="Carved totem head above a vertical spiral pattern in red"></div>
      <div class="bag__content">
        <div class="bag__kiwi" role="img" aria-label="Kiwi bird illustration in red"></div>
        <div class="bag__brand">Verdano</div>
        <div class="bag__sub">coffee co.</div>
        <div class="bag__label">SUPREME</div>
        <div class="bag__profile">
          <div class="bag__profile-title">CUP PROFILE:</div>
          <ul class="bag__notes"><li>Honey</li><li>Stonefruit</li><li>Toffee</li><li>Medium/high sweetness</li></ul>
        </div>
        <div class="bag__methods">
          <div class="method"><svg viewBox="0 0 30 30" fill="none" stroke="#ccc" stroke-width="2"><path d="M4 6h22L17 20h-4z"/><path d="M11 25h8"/></svg>Filter</div>
          <div class="method"><svg viewBox="0 0 30 30" fill="none" stroke="#ccc" stroke-width="2"><circle cx="9" cy="9" r="6"/><path d="M13 13l13 13"/></svg>Espresso</div>
          <div class="method"><svg viewBox="0 0 30 30" fill="none" stroke="#ccc" stroke-width="2"><rect x="8" y="8" width="14" height="19"/><path d="M15 2v12M10 3h10"/></svg>Plunger</div>
          <div class="method"><svg viewBox="0 0 30 30" fill="#ccc"><ellipse cx="11" cy="9" rx="5" ry="7"/><ellipse cx="20" cy="21" rx="5" ry="7"/></svg>Beans</div>
        </div>
        <div class="bag__url">www.verdanocoffee.co.nz</div>
        <div class="bag__weight">1Kg</div>
      </div>
    </div>
  </article>
</section>

<section class="brand-panel">
  <div class="brand-panel__totem brand-panel__totem--left" role="img" aria-label="Gold carved totem head above a koru carving"></div>
  <div class="brand-panel__totem brand-panel__totem--right" role="img" aria-label="Gold carved totem head above a koru carving"></div>
  <div class="brand-panel__kiwi" role="img" aria-label="Gold kiwi bird illustration"></div>
  <div class="brand-panel__name">Verdano</div>
  <div class="brand-panel__sub">coffee co.</div>
</section>

</body>
</html>
```